Flyer : Wolkenbank - Emphatisches Zuhören
Zielgruppe
Hallo und vielen Dank für dein Interesse an diesem Projekt.
Nachstehend ein paar Gedanken, die ein Gefühl für das Ziel des zu entwickelnden Flyers hervorrufen soll.
1. Warum gibt es Wolkenbank? (Das Fundament)
Das Problem:
In einer zunehmend beschleunigten und digitalen Welt vereinsamen Menschen – oft auch inmitten eines vollen Alltags. Freunde und Familie sind häufig überfordert, voreingenommen oder neigen dazu, sofort ungefragte Ratschläge zu verteilen, statt einfach nur zuzuhören.
Die Mission:
Wolkenbank.de bietet einen geschützten, wertfreien Raum, in dem Menschen einfach sein und reden dürfen. Es geht nicht um Therapie, sondern um das befreiende Gefühl, auf Augenhöhe gehört und verstanden zu werden. Der Name impliziert bereits die Gemütlichkeit und Sicherheit eines Sessels gepaart mit offenen Ohren.
2. Was leistet Wolkenbank?
Das Angebot:
- Professionelle Präsenz: Echtes, aktives und empathisches Zuhören ohne Bewertung.
- Entlastung: Raum für Gedanken und Gefühle, die man sonst nirgends aussprechen mag (Mental Load abbauen).
- Flexibilität: Niedrigschwelliger Zugang ohne monatelange Wartezeiten.
3. Zielgruppen-Matrix
Erwartung vs. Nutzen:
Für den Flyer ist es genial, die Zielgruppen direkt in ihren jeweiligen Bedürfnissen abzuholen. Hier ist eine Übersicht, die visuell übersetzt werden sollte.
Zielgruppe 1:
- Überlastete Berufstätige, Führungskräfte und Care-Arbeiter
Erwartung/Schmerzpunkt:
- „Ich funktioniere nur noch. Niemand hört mir zu, ohne dass es gleich um Lösungen geht.“
Der Wolkenbank-Nutzen:
- Ventil & Me-Time: Ein Raum, um den Ballast des Tages abzuwerfen, ganz ohne Erwartungsdruck.
Zielgruppe 2:
- Einsame oder ältere Menschen
- „Ich möchte einfach mal wieder ein echtes, tiefes Gespräch führen, das über das Wetter hinausgeht.“
Aufgabenstellung
Tonalität & Visuelle Identität (Look & Feel)
Empathisch, warm und einladend, aber hochgradig professionell. Der Flyer darf weder klinisch-kalt (wie eine Arztpraxis) noch esoterisch-verspielt wirken.
Farbpsychologie: Setzt auf beruhigende, vertrauenserweckende Töne (gern Orientierung an die Website), warme Erdtöne, sanftes Lila. Keine aggressiven Primärfarben (wie Knallrot oder Signalgelb).
Bildsprache: Vermeidet sterile Stockfotos von Menschen mit „Fake-Lächeln“. Besser sind authentische, ruhige Motive: Fokussierte Details (z. B. eine dampfende Tasse Kaffee, ein gemütlicher Sessel im Anschnitt) oder abstrakte Formen, die das Thema „Resonanz“ und „Zuhören“ symbolisieren (z. B. Wellenlinien, die sanft ineinandergreifen).
Format & Struktur des Flyers
Format: Eure Empfehlung, vielleicht ein 6-seitiger Wickelfalz-Flyer (DIN lang). Das könnte folgende Struktur ergeben:
Titelseite: Das Kernversprechen („Emphatisches Zuhören - Zeit und Raum für unvoreingenommenes Zuhören und Mitteilen) + Logo.
Innenseiten (3 Spalten): Perfekt, um die 3 oben genannten Zielgruppen getrennt voneinander mit ihren spezifischen Erwartungen und dem Wolkenbank-Nutzen anzusprechen.
Rückseite / Innere Klappe: Der Ablauf (Wie buche ich ein Gespräch?) und der klare Call to Action (CTA) inklusive Website-Adresse sowie Kontaktdaten.
Technische & Textliche Vorgaben
Barrierefreiheit & Lesbarkeit:
Da auch ältere Menschen zur Zielgruppe gehören, muss die Typografie klar, kontrastreich und ausreichend groß sein (keine filigranen Light-Schriften auf hellem Grund).
Auf dem Flyer kann ein prominenter Hinweis platziert werden, der Zugang zur Website (oder auch Infos eines Blogbeitrags mit weiteren Erklärungen zum Angebot) beinhaltet, z. B. via eines QR-Code, der die entsprechende URL enthält. Etwas, das man mitnehmen kann, wenn man den Flyer nicht einstecken möchte...

```html
<!DOCTYPE html>
<html lang="de">
<head>
<meta charset="utf-8">
<title>Wolkenbank – Flyer Innenseiten</title>
<link href="https://fonts.googleapis.com/css2?family=Lato:wght@400;700;900&family=Nunito+Sans:wght@400;600;700;800&display=swap" rel="stylesheet">
<style>
  :root{
    --page-bg:#e2e2df;
    --purple:#6a4c93;
    --purple-text:#7a5aa6;
    --rose:#b5566a;
    --rose-soft:#d07a8c;
    --pink-line:#d46aa8;
    --ink:#2b2530;
    --ink-soft:#4a4350;
    --panel-lilac-top:#f3f0f6;
    --panel-lilac-bottom:#dcd7e3;
    --panel-cream-top:#f7f3ee;
    --panel-cream-bottom:#ebe3da;
    --icon-bg:#efe3ee;
    --icon-bg-warm:#eedfd8;
  }
  *{box-sizing:border-box;margin:0;padding:0}
  html,body{width:1200px;height:1200px;overflow:hidden;background:var(--page-bg)}
  body{font-family:"Nunito Sans",sans-serif;color:var(--ink);position:relative}
  .flyer-inside{
    position:absolute;left:60px;top:200px;width:1080px;height:800px;
    display:flex;box-shadow:0 18px 40px rgba(60,50,70,.18);
  }
  .panel{
    width:360px;height:800px;position:relative;display:flex;flex-direction:column;
    padding:38px 34px 0;overflow:hidden;
  }
  .panel--lilac{background:linear-gradient(180deg,var(--panel-lilac-top),var(--panel-lilac-bottom))}
  .panel--cream{background:linear-gradient(180deg,var(--panel-cream-top),var(--panel-cream-bottom))}
  .panel + .panel{border-left:1px solid rgba(120,100,130,.18)}
  .audience-tag{
    align-self:flex-start;font-family:"Lato",sans-serif;font-weight:700;font-size:11px;
    letter-spacing:.08em;text-transform:uppercase;color:#fff;padding:6px 12px;
    background:var(--purple);border-radius:2px;
  }
  .panel--cream .audience-tag{background:var(--rose)}
  .headline{
    font-family:"Lato",sans-serif;font-weight:900;font-size:34px;line-height:1.08;
    color:var(--purple-text);margin-top:18px;
  }
  .headline-rule{width:34px;height:3px;background:var(--pink-line);border-radius:2px;margin-top:14px}
  .panel--cream .headline-rule{background:var(--rose-soft)}
  .topic-icon{
    width:110px;height:110px;border-radius:50%;background:var(--icon-bg);
    margin:26px auto 0;
  }
  .panel--cream .topic-icon{background:var(--icon-bg-warm)}
  .quote{
    font-weight:700;font-size:16px;line-height:1.45;color:var(--ink);
    margin-top:24px;text-align:center;
  }
  .benefit-label{display:flex;align-items:center;gap:12px;margin-top:24px}
  .benefit-badge{width:34px;height:34px;border-radius:50%;background:#c66fb8;display:flex;align-items:center;justify-content:center;flex:none}
  .panel--cream .benefit-badge{background:var(--rose-soft)}
  .benefit-label span{font-weight:700;font-size:13px;color:#a24fa0}
  .panel--cream .benefit-label span{color:var(--rose)}
  .benefit-title{font-weight:800;font-size:16px;color:var(--ink);margin-top:12px}
  .benefit-text{font-size:14px;line-height:1.5;color:var(--ink-soft);margin-top:6px}
  .panel-photo{position:absolute;left:0;right:0;bottom:0;height:230px}
  .photo--desk{background:linear-gradient(180deg,rgba(220,215,227,0),#c9b8b4 35%,#a89088)}
  .photo--cup{background:linear-gradient(180deg,rgba(235,227,218,0),#cbb59c 35%,#a77d58)}
  .photo--lake{background:linear-gradient(180deg,rgba(220,215,227,0),#c6b6d4 35%,#8a739e)}
</style>
</head>
<body>
<main class="flyer-inside">

  <section class="panel panel--lilac">
    <p class="audience-tag">Für Berufstätige &amp; Care-Arbeiter</p>
    <h2 class="headline">Ständig<br>unter Strom?</h2>
    <div class="headline-rule"></div>
    <div class="topic-icon" role="img" aria-label="Linienillustration: gestresste Person am Laptop"></div>
    <p class="quote">„Ich funktioniere nur noch. Niemand hört mir zu, ohne dass es gleich um Lösungen geht.“</p>
    <div class="benefit-label">
      <div class="benefit-badge"><svg width="18" height="16" viewBox="0 0 18 16"><path d="M9 15 L2 8 A4 4 0 0 1 9 3 A4 4 0 0 1 16 8 Z" fill="none" stroke="#fff" stroke-width="1.8" stroke-linejoin="round"/></svg></div>
      <span>Ihr Nutzen bei Wolkenbank</span>
    </div>
    <h3 class="benefit-title">Ventil &amp; Me-Time</h3>
    <p class="benefit-text">Ein Raum, um den Ballast des Tages abzuwerfen, ganz ohne Erwartungsdruck.</p>
    <div class="panel-photo photo--desk" role="img" aria-label="Foto: Tasse und Pflanze auf einem Schreibtisch mit Laptop"></div>
  </section>

  <section class="panel panel--cream">
    <p class="audience-tag">Für Ältere &amp; einsame Menschen</p>
    <h2 class="headline">Niemand da<br>zum Reden?</h2>
    <div class="headline-rule"></div>
    <div class="topic-icon" role="img" aria-label="Linienillustration: zwei Menschen im Gespräch"></div>
    <p class="quote">„Ich möchte einfach mal wieder ein echtes, tiefes Gespräch führen, das über das Wetter hinausgeht.“</p>
    <div class="benefit-label">
      <div class="benefit-badge"><svg width="18" height="16" viewBox="0 0 18 16"><path d="M9 15 L2 8 A4 4 0 0 1 9 3 A4 4 0 0 1 16 8 Z" fill="none" stroke="#fff" stroke-width="1.8" stroke-linejoin="round"/></svg></div>
      <span>Ihr Nutzen bei Wolkenbank</span>
    </div>
    <h3 class="benefit-title">Verbindung &amp; Wertschätzung</h3>
    <p class="benefit-text">Das Gefühl, dass die eigene Stimme und Geschichte noch zählen.</p>
    <div class="panel-photo photo--cup" role="img" aria-label="Foto: Kaffeetasse, Strickdecke und Brille auf Holztisch"></div>
  </section>

  <section class="panel panel--lilac">
    <p class="audience-tag">Für Menschen in Umbruchphasen</p>
    <h2 class="headline">Gedanken-<br>karussell im<br>Kopf?</h2>
    <div class="headline-rule"></div>
    <div class="topic-icon" role="img" aria-label="Linienillustration: verknäuelter Faden, der sich zu einem Pfeil löst"></div>
    <p class="quote">„Ich bin blockiert und muss meine Gedanken sortieren, will aber keine Ratschläge.“</p>
    <div class="benefit-label">
      <div class="benefit-badge"><svg width="18" height="16" viewBox="0 0 18 16"><path d="M9 15 L2 8 A4 4 0 0 1 9 3 A4 4 0 0 1 16 8 Z" fill="none" stroke="#fff" stroke-width="1.8" stroke-linejoin="round"/></svg></div>
      <span>Ihr Nutzen bei Wolkenbank</span>
    </div>
    <h3 class="benefit-title">Klarheit durch Resonanz</h3>
    <p class="benefit-text">Durch das Aussprechen im geschützten Raum ordnen sich die Gedanken von selbst.</p>
    <div class="panel-photo photo--lake" role="img" aria-label="Foto: einzelner Baum an einem nebligen See in Lilatönen"></div>
  </section>

</main>
</body>
</html>
```